Transform this table

Please make a 2 page A4 handout from this boring table into an engaging design. The front page can be simple and engaging (a summary of the back where all the detail lives)

Target Market(s)

Business

Requirements
Must have
• Clarity. And impact.
Nice to have
• Icons

```html
<!DOCTYPE html>
<html lang="en">
<head>
<meta charset="UTF-8">
<title>Safety Culture Maturity Ladder</title>
<link rel="stylesheet" href="https://fonts.googleapis.com/css2?family=Oswald:wght@600&family=Montserrat:wght@700&family=Roboto:wght@400&display=swap">
<style>
  :root{
    --maroon:#7b0b0d;
    --band:#8e1014;
    --red:#d9272e;
    --coral:#f26a38;
    --orange:#f7941d;
    --green:#8dc63f;
    --teal:#109b86;
    --green-text:#6aa82c;
    --column:#ededed;
    --ink:#3a3a3a;
    --paper:#ffffff;
    --backdrop:#e4e4e4;
  }
  *{box-sizing:border-box;margin:0;padding:0}
  html,body{width:1200px;height:1200px;overflow:hidden;background:var(--backdrop)}
  .poster{position:absolute;left:236px;top:86px;width:728px;height:1028px;background:var(--paper);box-shadow:0 4px 14px rgba(0,0,0,.18);overflow:hidden}
  .title-band{position:absolute;left:0;top:0;width:100%;height:67px;background:var(--maroon);display:flex;align-items:center;justify-content:center}
  .title-band h1{font-family:'Oswald',sans-serif;font-weight:600;font-size:40px;line-height:1;color:#fff;letter-spacing:.5px;transform:scaleX(.9);white-space:nowrap}
  .foot-band{position:absolute;left:0;bottom:0;width:100%;height:16px;background:var(--maroon)}
  .column{position:absolute;top:80px;width:127px;height:926px;background:var(--column)}
  .stage-head{position:absolute;left:0;top:0;width:100%;height:90px;display:flex;align-items:center;justify-content:center}
  .stage-head span{font-family:'Oswald',sans-serif;font-weight:600;font-size:28px;line-height:1;color:#fff;transform:scaleX(.8);white-space:nowrap}
  .traits,.practices{position:absolute;font-family:'Roboto',sans-serif;font-size:9px;line-height:10.4px;color:var(--ink);list-style:none;white-space:nowrap}
  .traits li,.practices li{position:relative;padding-left:7px}
  .traits li::before,.practices li::before{content:"•";position:absolute;left:0;color:var(--bullet)}
  .traits{left:8px;top:100px}
  .ladder{position:absolute;left:0;top:0;width:728px;height:1028px}
  .badge{position:absolute;width:127px;display:flex;flex-direction:column;align-items:center;border-radius:6px 6px 64px 64px;color:#fff;text-align:center}
  .badge svg{width:58px;height:58px;fill:none;stroke:#fff;stroke-width:3;stroke-linecap:round;stroke-linejoin:round}
  .badge p{font-family:'Montserrat',sans-serif;font-weight:700;font-size:15px;line-height:17px;white-space:nowrap}
  .culture{position:absolute;width:127px;text-align:center;font-family:'Montserrat',sans-serif;font-weight:700;font-size:15px;line-height:18px;white-space:nowrap}
  .culture small{display:block;font-size:11px;line-height:14px}
  .c1{left:17px;--bullet:var(--red)} .c2{left:154px;--bullet:var(--coral)} .c3{left:292px;--bullet:var(--orange)}
  .c4{left:430px;--bullet:var(--green)} .c5{left:566px;--bullet:var(--teal)}
  .p1{left:25px;--bullet:var(--red)} .p2{left:162px;--bullet:var(--coral)} .p3{left:300px;--bullet:var(--orange)}
  .p4{left:438px;--bullet:var(--green)} .p5{left:574px;--bullet:var(--teal)}
</style>
</head>
<body>
<div class="poster">
  <header class="title-band"><h1>SAFETY CULTURE MATURITY LADDER</h1></header>

  <section class="column c1">
    <div class="stage-head" style="background:var(--red)"><span>VULNERABLE</span></div>
    <ul class="traits">
      <li>Apathy / resistance</li><li>Near misses<br>not considered</li><li>Negligence</li><li>Dishonesty</li><li>Hiding of incidents</li><li>Serious injury<br>/ health risks are<br>unseen or ignored</li><li>Unfair disciplinary<br>actions</li><li>No or little training</li><li>Poor or<br>no communication</li><li>Production at almost<br>any cost</li><li>"Just get it done"<br>attitude or blatantly<br>unsafe</li>
    </ul>
  </section>
  <section class="column c2">
    <div class="stage-head" style="background:var(--coral)"><span>REACTIVE</span></div>
    <ul class="traits">
      <li>Dependent on<br>natural instincts</li><li>Accept need to care</li><li>Some near miss<br>reporting</li><li>Some window dressing<br>e.g. pre-inspection<br>cleanups and light duty</li><li>Disciplinary action</li><li>Minimum /<br>inconsistent training</li><li>Some communication<br>on a need to know<br>basis</li>
    </ul>
  </section>
  <section class="column c3">
    <div class="stage-head" style="background:var(--orange)"><span>COMPLIANT</span></div>
    <ul class="traits">
      <li>Supervision dependent</li><li>Some participation</li><li>Near miss discussions</li><li>Acceptable training<br>/ awareness</li><li>Established and good<br>communication<br>channels</li><li>Regular people<br>involvement and focus</li>
    </ul>
  </section>
  <section class="column c4">
    <div class="stage-head" style="background:var(--green)"><span>PROACTIVE</span></div>
    <ul class="traits">
      <li>Involvement at all levels</li><li>Near miss involvement</li><li>High level of training<br>/ awareness</li><li>Communication at<br>a high level<br>hiding nothing</li>
    </ul>
  </section>
  <section class="column c5">
    <div class="stage-head" style="background:var(--teal)"><span>RESILIENT</span></div>
    <ul class="traits">
      <li>Way of life</li><li>Comes natural</li><li>Personal involvement<br>by all to manage risks<br>well &amp; prevent incidents</li><li>Authentic<br>communication<br>throughout culture</li>
    </ul>
  </section>

  <svg class="ladder" viewBox="0 0 728 1028" aria-hidden="true">
    <polygon points="100,580 700,318 700,430 100,680" fill="var(--band)"/>
    <path d="M566,330 L544,330 L631,286 L718,330 L693,330 L693,438 A63.5,63.5 0 0 1 566,438 Z" fill="var(--teal)"/>
  </svg>

  <div class="badge" style="left:17px;top:526px;height:216px;background:var(--red);padding-top:24px">
    <svg viewBox="0 0 60 60"><circle cx="30" cy="30" r="22"/><line x1="15" y1="15" x2="45" y2="45"/></svg>
    <p style="margin-top:38px">ACCEPT<br>THAT<br>ACCIDENTS<br>HAPPEN</p>
  </div>
  <div class="culture c1" style="top:754px;color:var(--red)">TOXIC<br>/ NO CARE<br>CULTURE</div>
  <ul class="practices p1" style="top:823px">
    <li>Reactive or<br>unresponsive approach</li><li>No OHS systems</li><li>No risk assessment</li><li>Legal non compliance</li><li>Accept equipment<br>/ process decay</li><li>Only fix when broken<br>/ unsafe repairs</li><li>Reports are shelved<br>/ used irresponsibly</li><li>No or poor<br>investigation</li><li>No monitoring / audits</li><li>Permit non-compliance</li><li>Potential illegal practices</li>
  </ul>

  <div class="badge" style="left:154px;top:439px;height:228px;background:var(--coral);padding-top:32px">
    <svg viewBox="0 0 60 60"><line x1="8" y1="30" x2="50" y2="30"/><polyline points="38,18 50,30 38,42"/></svg>
    <p style="margin-top:36px">PREVENT<br>A SIMILAR<br>ACCIDENT</p>
  </div>
  <div class="culture c2" style="top:685px;color:var(--coral)">BLAME<br>CULTURE</div>
  <ul class="practices p2" style="top:736px">
    <li>Administrator driven</li><li>Loose systems, elements<br>of an OHS Management<br>System</li><li>Reactive risk assessment<br>and control</li><li>Minimum legal<br>compliance</li><li>Apply PPE as a way of<br>eliminating exposure</li><li>Incident investigation<br>but limited analysis</li><li>Focus on what<br>happened</li><li>No systems focus</li><li>Human faults occur</li><li>Ad hoc monitoring<br>/ audits</li><li>No occupational hygiene<br>or health initiatives</li><li>Reactive medical<br>monitoring</li><li>Monitoring as per<br>regulations</li>
  </ul>

  <div class="badge" style="left:292px;top:402px;height:220px;background:var(--orange);padding-top:16px">
    <svg viewBox="0 0 60 60" style="width:64px;height:64px"><rect x="13" y="10" width="34" height="44" rx="3"/><rect x="23" y="6" width="14" height="8" rx="2"/><polyline points="19,24 22,27 27,21"/><line x1="31" y1="24" x2="41" y2="24"/><polyline points="19,34 22,37 27,31"/><line x1="31" y1="34" x2="41" y2="34"/><polyline points="19,44 22,47 27,41"/><line x1="31" y1="44" x2="41" y2="44"/></svg>
    <p style="margin-top:26px">WRITE AND<br>ENFORCE<br>PROCEDURES</p>
  </div>
  <div class="culture c3" style="top:640px;color:var(--orange)">COMPLIANCE<br>CULTURE</div>
  <ul class="practices p3" style="top:694px">
    <li>OHS coordinator driven</li><li>OHS standards system<br>and ISO 9002 or<br>equivalent</li><li>Risk assessment through<br>existing systems</li><li>Total legal compliance<br>goal</li><li>Strictly enforced the use<br>of PPE where required<br>(knowing risk)</li><li>Causal incident analysis<br>based on events<br>potential</li><li>Info sharing from events</li><li>Planned occupational<br>hygiene / environmental<br>monitoring</li><li>Periodical medical<br>examinations</li><li>Planned monitoring<br>/ audits</li><li>Safety meetings &amp; talks</li><li>Some task observations</li>
  </ul>

  <div class="badge" style="left:430px;top:343px;height:212px;background:var(--green);padding-top:16px">
    <svg viewBox="0 0 60 60" style="width:64px;height:64px"><path d="M22 30a10 10 0 1 1 16 0c-2 2-3 4-3 6h-10c0-2-1-4-3-6z"/><line x1="25" y1="41" x2="35" y2="41"/><line x1="30" y1="4" x2="30" y2="8"/><line x1="14" y1="12" x2="17" y2="15"/><line x1="46" y1="12" x2="43" y2="15"/><line x1="12" y1="52" x2="48" y2="52"/><line x1="30" y1="44" x2="30" y2="52"/></svg>
    <p style="margin-top:45px">MANAGE<br>RISKS<br>WELL</p>
  </div>
  <div class="culture c4" style="top:568px;color:var(--green-text)">INDEPENDENT<br>&amp; PERSONAL<br>OWNERSHIP<br>CULTURE</div>
  <ul class="practices p4" style="top:654px">
    <li>Committed leadership<br>at all levels</li><li>Line driven systems<br>improvement</li><li>ISO 14001 &amp; ISO 45001</li><li>Pro-active formal risk<br>management</li><li>Beyond legal compliance</li><li>Seek to actively<br>engineer out process /<br>equipment inadequacies</li><li>Incident learnings<br>shared with all levels</li><li>Well designed plans<br>/ procedures</li><li>Focus on adhering to<br>site plans &amp; procedures</li><li>Integrated audits</li><li>Peer evaluations<br>and discussion</li>
  </ul>

  <div class="badge" style="left:566px;top:330px;height:172px;background:transparent;padding-top:4px">
    <svg viewBox="0 0 60 60" style="width:64px;height:64px"><polyline points="10,50 22,50 22,42 32,42 32,34 42,34 42,26 52,26"/><line x1="46" y1="26" x2="46" y2="8"/><polyline points="46,8 56,12 46,16"/></svg>
    <p style="margin-top:28px">WAY WE DO<br>BUSINESS</p>
  </div>
  <div class="culture c5" style="top:522px;color:var(--teal)"><small>INTERDEPENDENT</small>TEAM<br>CULTURE</div>
  <ul class="practices p5" style="top:592px">
    <li>Individually internalized</li><li>Inspiring genuine<br>leadership</li><li>No silo thinking or<br>actions</li><li>All staff active, positive,<br>respected, speaking up</li><li>Excellent equipment,<br>ultra-organised</li><li>Integrated management<br>systems</li><li>Risk management cycle<br>integrated into all<br>systems</li><li>Self regulating style</li><li>Eliminate &amp; prevent<br>problems before they<br>occur</li><li>All threats considered<br>in decision-making</li><li>Continually improving<br>through external<br>evaluation / auditing</li><li>Multiple positive<br>performance indicators<br>drive PDCA cycle</li>
  </ul>

  <div class="foot-band"></div>
</div>
</body>
</html>
```